New Van wrap for fertilization and pest control side

We are an existing landscape construction company, growing our fertilzation and pest control side of the business, and looking to add a standard wrap or vinyl to our new fert vans. We want to see bright colors that grab vision to the vehicles, we have large box trucks for out landscape maintenance crews which do a nice job but really want people to recognize these vans for fertilization and pest control
Target Market(s)
people driven for quality service and safe for their home and kids
Requirements
Must have
- bright colors, must send the message that we are a safe fertilization and pest control company
Nice to have
- could use a cartoon character or animal dressed up to show the service
Should not have
- not to wordy going on large vans, our company name is Ridgefold Landscape but we do own the url RF fert if you think that is something that would make sense

```html
<!DOCTYPE html>
<html lang="en">
<head>
<meta charset="utf-8">
<title>Ridgefold Landscape – Fert Van Side Wrap</title>
<link rel="stylesheet" href="https://fonts.googleapis.com/css2?family=Josefin+Sans:wght@700&family=Open+Sans:wght@400;600&display=swap">
<style>
  :root {
    --backdrop: #e4e5e6;
    --wrap-green: #4a8a24;
    --wrap-green-dark: #3d7a1c;
    --wrap-black: #1b1c1c;
    --stripe-light: #d9dadb;
    --accent-green: #7dc242;
    --text-white: #ffffff;
    --art-orange: #e8a23a;
    --art-blue: #7ec3e8;
  }
  html, body {
    margin: 0;
    padding: 0;
    width: 1200px;
    height: 1200px;
    overflow: hidden;
    background: var(--backdrop);
  }
  .canvas { display: block; width: 1200px; height: 1200px; }
  .wrap-green { fill: var(--wrap-green); }
  .wrap-green-dark { fill: var(--wrap-green-dark); }
  .wrap-black { fill: var(--wrap-black); }
  .wrap-stripe { fill: var(--stripe-light); }
  .tagline-band { fill: var(--wrap-green); }
  .service-title {
    font-family: "Josefin Sans", sans-serif;
    font-weight: 700;
    font-size: 31px;
    letter-spacing: 1px;
    fill: var(--text-white);
  }
  .web-address {
    font-family: "Open Sans", sans-serif;
    font-weight: 400;
    font-size: 30px;
    fill: var(--text-white);
  }
  .company-name {
    font-family: "Open Sans", sans-serif;
    font-weight: 600;
    font-size: 40px;
    fill: var(--text-white);
  }
  .tagline {
    font-family: "Open Sans", sans-serif;
    font-weight: 400;
    font-size: 11.5px;
    fill: var(--text-white);
  }
  .phone-number {
    font-family: "Open Sans", sans-serif;
    font-weight: 400;
    font-size: 31px;
    fill: var(--accent-green);
  }
</style>
</head>
<body>
<svg class="canvas" viewBox="0 0 1200 1200" xmlns="http://www.w3.org/2000/svg">
  <defs>
    <clipPath id="wrap-outline">
      <rect x="40" y="380" width="1120" height="440" rx="28"/>
    </clipPath>
    <linearGradient id="mascot-tones" x1="0" y1="0" x2="0" y2="1">
      <stop offset="0" stop-color="var(--art-orange)"/>
      <stop offset="0.6" stop-color="var(--art-orange)"/>
      <stop offset="1" stop-color="var(--art-blue)"/>
    </linearGradient>
  </defs>

  <g class="wrap-panel" clip-path="url(#wrap-outline)">
    <rect class="wrap-green" x="40" y="380" width="1120" height="440"/>
    <polygon class="wrap-stripe" points="581,380 615,380 834,760 800,760"/>
    <polygon class="wrap-black" points="615,380 1160,380 1160,820 834,820 834,760"/>
    <rect class="wrap-black" x="306" y="757" width="854" height="47"/>
    <rect class="wrap-green-dark" x="40" y="804" width="794" height="16"/>
    <polygon class="tagline-band" points="848,565 1130,565 1130,605 822,605"/>
  </g>

  <rect class="mascot-art" x="585" y="398" width="165" height="330" rx="36"
        fill="url(#mascot-tones)" role="img"
        aria-label="Cartoon pest control technician with a backpack sprayer giving a thumbs up, standing over a defeated bug"/>

  <text class="service-title" x="312" y="697">PEST CONTROL</text>
  <text class="web-address" x="340" y="791">www.ridgefoldlandscape.com</text>

  <text class="company-name" x="772" y="472">Ridgefold</text>
  <text class="company-name" x="852" y="522">Landscape</text>

  <text class="tagline" x="856" y="590">we are a safe fertilization &amp; pest control company</text>

  <text class="phone-number" x="838" y="642">(000.000.0000)</text>
</svg>
</body>
</html>
```